Law Offices business card

Hi there, I'll need business card for the Law Offices of Tobin Haskell. The information must convey his strategic approach and quick resolution to complex business litigation needs. Please emphasize Civil Litigation, Corporate Law, Business Governance and Real Estate Law. Tobin has over 25 years of experience in these fields.The card should be modern and edgy and the message should be clear. Please consult his current website for ideas.

Business

```html
<!DOCTYPE html>
<html lang="en">
<head>
<meta charset="utf-8">
<title>Tobin Haskell, PA — Business Card</title>
<link rel="stylesheet" href="https://fonts.googleapis.com/css2?family=Tinos:ital,wght@0,400;0,700;1,400&display=swap">
<style>
  :root {
    --leather-dark: #4a1410;
    --leather-mid: #6e241c;
    --leather-light: #84342a;
    --panel-ink: #ebe7e2;
    --panel-ink-soft: #d9c9c2;
    --cream: #fdf9d6;
    --ink: #1c1a17;
    --claret: #8e1010;
  }
  html, body {
    margin: 0;
    padding: 0;
    width: 1200px;
    height: 343px;
    overflow: hidden;
    background: #ffffff;
  }
  .card {
    width: 1200px;
    height: 343px;
    display: flex;
    font-family: "Tinos", "Times New Roman", serif;
  }
  .brand-panel {
    position: relative;
    width: 601px;
    height: 343px;
    background: radial-gradient(ellipse at 35% 45%, var(--leather-light) 0%, var(--leather-mid) 45%, var(--leather-dark) 100%);
  }
  .brand-block {
    position: absolute;
    left: 112px;
    top: 90px;
    right: 40px;
    color: var(--panel-ink);
  }
  .firm-name {
    margin: 0;
    font-weight: 400;
    color: var(--panel-ink);
  }
  .firm-line {
    display: block;
    font-size: 22px;
    letter-spacing: 1.5px;
    text-transform: uppercase;
    line-height: 1;
  }
  .principal {
    display: block;
    font-size: 58px;
    line-height: 62px;
    margin-top: 12px;
  }
  .positioning {
    margin: 22px 0 0;
    padding-top: 14px;
    border-top: 1px solid var(--panel-ink-soft);
    width: 400px;
    font-size: 16px;
    line-height: 22px;
    letter-spacing: 0.5px;
    color: var(--panel-ink-soft);
  }
  .details-panel {
    flex: 1;
    height: 343px;
    background: var(--cream);
    text-align: center;
    position: relative;
  }
  .attorney-name {
    margin: 0;
    padding-top: 26px;
    font-size: 30px;
    font-weight: 400;
    color: var(--ink);
    line-height: 1;
    letter-spacing: 0.5px;
  }
  .attorney-title {
    margin: 3px 0 0;
    font-size: 14px;
    color: var(--ink);
    letter-spacing: 0.5px;
  }
  .practice-areas {
    list-style: none;
    margin: 34px 0 0;
    padding: 0;
    color: var(--claret);
    font-size: 23px;
    line-height: 26px;
    text-transform: uppercase;
  }
  .practice-areas li + li { margin-top: 10px; }
  .contact {
    position: absolute;
    left: 0;
    right: 0;
    top: 250px;
    margin: 0;
    font-style: italic;
    font-size: 16.5px;
    line-height: 24px;
    color: var(--ink);
  }
</style>
</head>
<body>
  <div class="card">
    <section class="brand-panel" role="img" aria-label="Dark red leather texture backdrop behind the firm name">
      <div class="brand-block">
        <h1 class="firm-name">
          <span class="firm-line">Law Offices of</span>
          <span class="principal">Tobin Haskell, PA</span>
        </h1>
        <p class="positioning">Strategic counsel &amp; quick resolution of complex business litigation &bull; Over 25 years of experience</p>
      </div>
    </section>
    <section class="details-panel">
      <h2 class="attorney-name">TOBIN HASKELL</h2>
      <p class="attorney-title">ATTORNEY</p>
      <ul class="practice-areas">
        <li>Civil Litigation &bull; Corporate Law</li>
        <li>Business Governance and<br>Real Estate Law</li>
        <li>Title and Closing Services</li>
      </ul>
      <p class="contact">
        518B Harbor Lane Palm Beach, Florida 33480<br>
        561-555-0148 &bull; 561-555-0193<br>
        tobin@tobinlaw.com &bull; www.tobinlaw.com
      </p>
    </section>
  </div>
</body>
</html>
```